We are a local Communty Pharmacy wishing to promote and market a specialised Pharmaceutical Service

We would like a design that is professional and enticing ( according to the brief In attached files)
We wish to Market Compounding Pharmacy as a specialist side of our business.
We have the expertise a purpose built preparation laboratory.
The main purpose is an Internet presence that entices prospective patients to contact or visit our physical store.

Target Market(s)

Patients Medicos and Veterinary clients

Industry/Entity Type

Pharmacy

Coding

Coded - Design and coding required

Number of Pages Required

1 page

Requirements
Must have
• Clear friendly image
Nice to have
• soft enticing feel
Should not have
• No crass loud unprofessional elements

```html
<!DOCTYPE html>
<html lang="en">
<head>
<meta charset="utf-8">
<title>Westbrook Compounding Pharmacy</title>
<link href="https://fonts.googleapis.com/css2?family=Open+Sans:wght@400;600;700&family=Roboto:wght@500;700;900&display=swap" rel="stylesheet">
<style>
:root{
  --navy:#0d3a6b;
  --blue:#1e88c9;
  --sky:#d6ecf8;
  --ink:#333b44;
  --muted:#6b737c;
  --green:#2fa84f;
  --cardblue:#1d8fd6;
  --orange:#f4a11a;
  --panel:#efefef;
  --line:#d9dde1;
  --white:#ffffff;
}
*{margin:0;padding:0;box-sizing:border-box}
html,body{width:698px;height:1200px;overflow:hidden;background:var(--white)}
body{font-family:"Open Sans",Arial,sans-serif;color:var(--ink);position:relative}
.topbar{height:12px;background:var(--navy);color:#cfe3f3;font-size:5px;display:flex;justify-content:flex-end;align-items:center;gap:14px;padding:0 30px}
.topbar span{display:flex;align-items:center;gap:3px}
.header{height:30px;display:flex;align-items:center;justify-content:space-between;padding:0 30px;border-bottom:1px solid var(--line)}
.brand{display:flex;align-items:center;gap:6px;font-family:"Roboto",sans-serif;font-weight:700;font-size:11px;color:var(--navy)}
.brand-mark{width:12px;height:12px;background:var(--blue);border-radius:50%}
.nav{display:flex;gap:18px;font-family:"Roboto",sans-serif;font-size:6px;font-weight:500;color:var(--ink)}
.nav .active{color:var(--blue)}
.hero{position:relative;height:220px;background:linear-gradient(100deg,#9fb4c4 0%,#dfe8ee 45%,#f4f7f9 70%,#c9d6df 100%)}
.hero-copy{position:absolute;left:0;right:0;top:128px;text-align:center}
.hero-title{font-family:"Roboto",sans-serif;font-weight:900;font-size:28px;color:var(--navy);letter-spacing:.3px}
.hero-sub{display:inline-block;margin-top:4px;background:var(--sky);color:var(--blue);font-size:8px;font-weight:600;padding:3px 22px;letter-spacing:.4px}
.hero-arrow{position:absolute;top:100px;width:14px;height:20px}
.hero-arrow.left{left:10px}.hero-arrow.right{right:10px}
.about{padding:26px 60px 0}
.section-title{font-family:"Roboto",sans-serif;font-weight:700;font-size:13px;color:var(--navy);text-align:center}
.rule{width:40px;height:2px;background:var(--blue);margin:6px auto 14px}
.about p{font-size:6.6px;line-height:11px;color:var(--muted);margin-bottom:10px}
.features{padding:8px 60px 0}
.cards{display:flex;gap:12px}
.card{flex:1}
.card-top{height:84px;display:flex;flex-direction:column;align-items:center;justify-content:center;gap:8px;color:var(--white);font-family:"Roboto",sans-serif;font-weight:700;font-size:10px}
.card.vet .card-top{background:var(--green)}
.card.scar .card-top{background:var(--cardblue)}
.card.thyroid .card-top{background:var(--orange)}
.card p{font-size:6px;line-height:9px;color:var(--muted);text-align:center;padding:6px 14px 0}
.info{position:absolute;left:0;right:0;top:790px;height:374px;background:var(--panel);padding:120px 60px 0;display:flex;gap:30px}
.info-col{flex:1}
.info h3{font-family:"Roboto",sans-serif;font-weight:700;font-size:10px;color:var(--ink);margin-bottom:10px}
.info p{font-size:6px;line-height:9px;color:var(--muted)}
.time-row{display:flex;align-items:center;gap:6px;font-size:7px;font-weight:600;color:var(--ink);margin-top:10px}
.map{height:110px;background:linear-gradient(135deg,#e6e2d6,#cfe0ea)}
.contact-row{display:flex;gap:6px;font-size:6px;line-height:9px;color:var(--muted);margin-bottom:10px}
.contact-row svg{flex:none}
.footer{position:absolute;left:0;right:0;bottom:0;height:36px;background:var(--navy);color:#cfe3f3;font-size:6px;display:flex;align-items:center;padding:0 60px;letter-spacing:.3px}
</style>
</head>
<body>
<div class="topbar">
  <span><svg width="5" height="6" viewBox="0 0 10 12"><path d="M5 0a4 4 0 0 0-4 4c0 3 4 8 4 8s4-5 4-8a4 4 0 0 0-4-4z" fill="#cfe3f3"/></svg>14 HARBOUR LANE, WESTBROOK WA 6000</span>
  <span><svg width="5" height="5" viewBox="0 0 10 10"><path d="M2 0l2 2-1 2c1 1 2 2 3 3l2-1 2 2-2 2C4 10 0 6 0 2z" fill="#cfe3f3"/></svg>08 5550 1234</span>
  <span>compounding@westbrookpharmacy.example</span>
</div>
<header class="header">
  <div class="brand"><span class="brand-mark"></span>Westbrook Compounding Pharmacy</div>
  <nav class="nav"><span class="active">HOME</span><span>ABOUT US</span><span>LOCATIONS</span><span>TIMINGS</span><span>CONTACT</span></nav>
</header>
<section class="hero" role="img" aria-label="Pharmacist in gloves preparing a compounded medicine in the laboratory">
  <svg class="hero-arrow left" viewBox="0 0 14 20"><path d="M10 3L4 10l6 7" stroke="#fff" stroke-width="2" fill="none"/></svg>
  <svg class="hero-arrow right" viewBox="0 0 14 20"><path d="M4 3l6 7-6 7" stroke="#fff" stroke-width="2" fill="none"/></svg>
  <div class="hero-copy">
    <div class="hero-title">COMPOUNDING PHARMACY IS</div>
    <div class="hero-sub">CUSTOMISED MEDICATIONS FOR PATIENTS</div>
  </div>
</section>
<section class="about">
  <h2 class="section-title">WHAT IS COMPOUNDING PHARMACY?</h2>
  <div class="rule"></div>
  <p>Naturally it is nothing new. The practice of making up medicines to suit each patient dates back over many centuries and was once the everyday work of every pharmacist before the rise of large scale drug manufacturing in the middle of the last century.</p>
  <p>That craft has quietly returned as doctors, patients and carers look for options that mass produced products cannot offer, such as altered strengths, removed allergens and new dosage forms.</p>
  <p>We are not dismissing the great value of commercial medicines, which are well tested and widely trusted, but for some people a standard product simply does not fit and a tailored preparation is the better answer.</p>
  <p>Compounding Pharmacy as such has recently emerged as new techniques and equipment allow our pharmacists to prepare creams, capsules, troches and liquids to precise doses in a clean, purpose built preparation laboratory under strict quality controls.</p>
  <p>The team are highly trained and work closely with your doctor or veterinarian, so every formula is checked, recorded and explained before it leaves our counter for your home.</p>
  <p>As a dedicated community pharmacy we feel we are uniquely placed to combine personal care with modern compounding skills and we are committed to meeting the needs of each patient who walks through our door.</p>
  <p>Our ultimate goal as a local pharmacy is helping our patients feel better, with medicines made for them. Visit us in store or call our compounding team to talk about your needs today.</p>
</section>
<section class="features">
  <h2 class="section-title">FEATURE ITEMS</h2>
  <div class="rule"></div>
  <div class="cards">
    <article class="card vet">
      <div class="card-top"><svg width="24" height="24" viewBox="0 0 24 24"><circle cx="12" cy="12" r="10" fill="none" stroke="#fff" stroke-width="2"/><path d="M12 7v10M7 12h10" stroke="#fff" stroke-width="2"/></svg>VET ARTICLE</div>
      <p>Flavoured, easy to give doses for pets of every size, prepared to your vet's script.</p>
    </article>
    <article class="card scar">
      <div class="card-top"><svg width="24" height="24" viewBox="0 0 24 24"><circle cx="12" cy="12" r="10" fill="none" stroke="#fff" stroke-width="2"/><path d="M7 12l3 3 7-7" stroke="#fff" stroke-width="2" fill="none"/></svg>SCAR THERAPY</div>
      <p>Gentle gels and creams made to soften and fade scars, matched to your skin type.</p>
    </article>
    <article class="card thyroid">
      <div class="card-top"><svg width="24" height="24" viewBox="0 0 24 24"><circle cx="12" cy="12" r="10" fill="none" stroke="#fff" stroke-width="2"/><circle cx="12" cy="12" r="3" fill="#fff"/></svg>THYROID EXTRACT</div>
      <p>Capsules measured to the exact strength your doctor requests, checked for every batch.</p>
    </article>
  </div>
</section>
<section class="info">
  <div class="info-col">
    <h3>TIMINGS</h3>
    <p>Open six days a week with a pharmacist on hand to help you.</p>
    <div class="time-row"><svg width="8" height="8" viewBox="0 0 10 10"><circle cx="5" cy="5" r="4" fill="none" stroke="#1e88c9" stroke-width="1.2"/><path d="M5 2.5V5h2" stroke="#1e88c9" fill="none"/></svg>7 DAYS A WEEK</div>
    <div class="time-row"><svg width="8" height="8" viewBox="0 0 10 10"><circle cx="5" cy="5" r="4" fill="none" stroke="#1e88c9" stroke-width="1.2"/><path d="M5 2.5V5h2" stroke="#1e88c9" fill="none"/></svg>8.30 AM TO 8.30 PM</div>
  </div>
  <div class="info-col">
    <h3>LOCATION</h3>
    <div class="map" role="img" aria-label="Street map showing the pharmacy location"></div>
  </div>
  <div class="info-col">
    <h3>CONTACT</h3>
    <div class="contact-row"><svg width="7" height="8" viewBox="0 0 10 12"><path d="M5 0a4 4 0 0 0-4 4c0 3 4 8 4 8s4-5 4-8a4 4 0 0 0-4-4z" fill="#1e88c9"/></svg><span>WESTBROOK COMPOUNDING PHARMACY<br>14 HARBOUR LANE<br>WESTBROOK WA 6000</span></div>
    <div class="contact-row"><svg width="7" height="7" viewBox="0 0 10 10"><path d="M2 0l2 2-1 2c1 1 2 2 3 3l2-1 2 2-2 2C4 10 0 6 0 2z" fill="#1e88c9"/></svg><span>08 5550 1234</span></div>
    <div class="contact-row"><svg width="8" height="6" viewBox="0 0 10 7"><rect x=".5" y=".5" width="9" height="6" fill="none" stroke="#1e88c9"/><path d="M.5.5L5 4l4.5-3.5" stroke="#1e88c9" fill="none"/></svg><span>compounding@westbrookpharmacy.example</span></div>
  </div>
</section>
<footer class="footer">© 2015 COMPOUNDING PHARMACY &nbsp;|&nbsp; ALL RIGHTS RESERVED</footer>
</body>
</html>
```